Oakfield crest Letter head

Need a heeder and footer for 8.5 x 11 paper
2 inch top header, 1.5 inch bottom footer
Add logo, agent pictures, names and titles (Broker), office picture with address
Oakfield Crest Real Estate
28317 Route 412
Cedar Hollow, SC 29614
Please make phone # large (555) 382-0617
OakfieldCrestRealEstate.com

```html
<!DOCTYPE html>
<html lang="en">
<head>
<meta charset="utf-8">
<title>Oakfield Crest Real Estate Letterhead</title>
<link href="https://fonts.googleapis.com/css2?family=Lato:wght@400;700;900&family=Montserrat:wght@400&display=swap" rel="stylesheet">
<style>
  :root {
    --navy: #1f1b54;
    --red: #c0202a;
    --paper: #f4f4f4;
    --backdrop: #dedede;
    --ink: #1a1a1a;
    --white: #ffffff;
    --lawn: #cfd3bd;
  }
  * { margin: 0; padding: 0; box-sizing: border-box; }
  html, body {
    width: 1200px; height: 1141px; overflow: hidden;
    background: var(--backdrop);
  }
  .letterhead {
    position: absolute; left: 170px; top: 18px;
    width: 860px; height: 1105px;
    background: var(--paper);
    overflow: hidden;
    box-shadow: 0 6px 18px rgba(0,0,0,.18);
    font-family: "Lato", sans-serif;
  }
  .top-bands { position: absolute; left: 0; top: 0; width: 860px; height: 22px; }

  .brand {
    position: absolute; left: 70px; top: 82px; width: 204px;
    text-align: center; color: var(--navy);
    font-family: "Lato", sans-serif; font-weight: 700;
  }
  .brand-mark {
    display: block; width: 22px; height: 22px; margin: 0 auto 10px;
    background: var(--navy);
  }
  .brand-name { display: block; font-size: 25px; line-height: 1.05; letter-spacing: .5px; }
  .brand-sub { display: block; font-size: 15px; letter-spacing: 4px; margin-top: 4px; }

  .agent { position: absolute; left: 660px; top: 42px; width: 138px; text-align: center; }
  .agent-photo {
    display: block; width: 113px; height: 114px; margin: 0 auto;
    border-radius: 9px; border: 2px solid #b9bcc4;
    background: radial-gradient(circle at 50% 45%, #3b7fd0 0%, #1d5db5 60%, #15448c 100%);
  }
  .agent-name { margin-top: 10px; font-size: 18px; font-weight: 900; color: var(--navy); white-space: nowrap; margin-left: -20px; margin-right: -20px; }
  .agent-title { font-size: 14px; color: var(--red); margin-top: 2px; }

  .letter { position: absolute; left: 78px; width: 715px; color: var(--ink); }
  .salutation { top: 251px; font-size: 18px; }
  .date { top: 296px; font-size: 16px; }
  .body-text {
    top: 340px;
    font-family: "Montserrat", sans-serif; font-size: 13px; line-height: 18.5px;
    text-align: justify;
  }
  .body-text p { margin-bottom: 18.5px; }
  .closing { top: 806px; font-size: 16px; z-index: 2; }

  .office-photo {
    position: absolute; left: 0; top: 745px; width: 860px; height: 360px;
    background:
      linear-gradient(180deg, var(--paper) 0%, rgba(244,244,244,.85) 25%, rgba(244,244,244,.35) 55%, rgba(244,244,244,0) 75%),
      linear-gradient(90deg, #c9cbd1 0%, #b9c3d8 35%, #c3cbdc 65%, #b7bfaf 100%);
  }
  .office-photo::after {
    content: ""; position: absolute; left: 0; right: 0; bottom: 0; height: 90px;
    background: linear-gradient(180deg, rgba(207,211,189,0) 0%, var(--lawn) 100%);
  }

  .footer-bands { position: absolute; left: 0; top: 1026px; width: 860px; height: 68px; }
  .phone {
    position: absolute; left: 72px; top: 1030px;
    font-size: 28px; font-weight: 700; color: var(--white);
  }
  .address {
    position: absolute; left: 72px; top: 1066px;
    font-size: 19.5px; color: var(--white); white-space: nowrap;
  }
  .website {
    position: absolute; right: 51px; top: 1060px;
    font-size: 19.5px; color: var(--white);
  }
</style>
</head>
<body>
<main class="letterhead">
  <svg class="top-bands" viewBox="0 0 860 22" aria-hidden="true">
    <polygon points="0,0 474,0 460,14 0,14" fill="var(--navy)"/>
    <polygon points="465,0 860,0 860,22 498,22" fill="var(--red)"/>
  </svg>

  <div class="brand">
    <span class="brand-mark"></span>
    <span class="brand-name">Oakfield Crest</span>
    <span class="brand-sub">Real Estate</span>
  </div>

  <div class="agent">
    <span class="agent-photo" role="img" aria-label="Portrait photo of the broker"></span>
    <div class="agent-name">DANA WHITFIELD</div>
    <div class="agent-title">Broker</div>
  </div>

  <div class="office-photo" role="img" aria-label="Photo of the office building with parking lot and lawn"></div>

  <p class="letter salutation">Dear Gordon</p>
  <p class="letter date">Date : 11 October 2020</p>

  <div class="letter body-text">
    <p>Lorem ipsum dolor sit amet, consectetur adipisicing elit, sed do eiusmod tempor incididunt ut labore et dolore magna aliqua. Ut enim ad minim veniam, quis nostrud exercitation ullamco laboris nisi ut aliquip ex ea commodo consequat. Duis aute irure dolor in reprehenderit in voluptate velit esse cillum dolore eu fugiat nulla pariatur. Excepteur sint occaecat cupidatat non proident, sunt in culpa qui officia deserunt mollit anim id est laborum. re et dolore magnam aliquam quaerat voluptatem.</p>
    <p>Lorem ipsum dolor sit amet, consectetur adipisicing elit, sed do eiusmod tempor incididunt ut labore et dolore magna aliqua. Ut enim ad minim veniam, quis nostrud exercitation ullamco laboris nisi ut aliquip ex ea commodo consequat. Duis aute irure dolor in reprehenderit in voluptate velit esse cillum dolore eu fugiat nulla pariatur. Excepteur sint occaecat cupidatat non proident, sunt in culpa qui officia deserunt mollit anim id est laborum. re et dolore magnam aliquam quaerat voluptatem.</p>
    <p>Lorem ipsum dolor sit amet, consectetur adipisicing elit, sed do eiusmod tempor incididunt ut labore et dolore magna aliqua. Ut enim ad minim veniam, quis nostrud exercitation ullamco laboris nisi ut aliquip ex ea commodo consequat.</p>
    <p>Lorem ipsum dolor sit amet, consectetur adipisicing elit, sed do eiusmod tempor incididunt ut labore et dolore magna aliqua. Ut enim ad minim veniam, quis nostrud exercitation ullamco laboris nisi ut aliquip ex ea commodo consequat.</p>
    <p>Lorem ipsum dolor sit amet, consectetur adipisicing elit, sed do eiusmod tempor incididunt ut labore et dolore magna aliqua. Ut enim ad minim veniam, quis nostrud exercitation ullamco laboris nisi ut aliquip ex ea commodo consequat.</p>
  </div>

  <p class="letter closing">Regards</p>

  <svg class="footer-bands" viewBox="0 0 860 68" aria-hidden="true">
    <polygon points="0,0 488,0 541,68 0,68" fill="var(--navy)"/>
    <polygon points="521,26 860,26 860,68 553,68" fill="var(--red)"/>
  </svg>
  <div class="phone">Call us : (555) 382-0617</div>
  <div class="address">28317 Route 412, Cedar Hollow, SC 29614</div>
  <div class="website">OakfieldCrestRealEstate.com</div>
</main>
</body>
</html>
```